Lumora.io Homepage Redesign

We are seeking a talented designer to create an emotive and aspirational homepage for our website (www.lumora.io) that elevates the Lumora.io brand using our new home page copy.

Our current design feels product-heavy and lacks the global, professional, and emotive touch we're aiming for.

We want to strip back unnecessary visual distractions and focus on a more streamlined, compelling design that resonates with our audience.

Project Goals:
Replace product-heavy, literal imagery with more evocative, aspirational visuals.
Create a homepage that feels aspirational and professional, reflecting our global ambitions.
Explore the use of icons or simple graphics to reduce visual clutter and create a more refined experience.
Ensure that usability principles are at the forefront of the design. Navigation must be clear and accessible on both desktop and mobile.
Practicality is key. Any animations or transitions should serve a functional purpose and should not hinder website speed or performance.
We prefer mockups in Adobe XD for ease of use by our developer, but Photoshop is also acceptable if this suits your workflow better.

Design Considerations:
Imagery: The selected imagery should enhance the emotive feel of the site, not simply fill space.
Usability: Avoid hidden navigation on desktop, and ensure key call-to-action buttons like "Watch Demo" and "Book a Demo" are clearly identifiable as clickable.
Animations/Transitions: Any animated elements should focus on showcasing our content, not just adding visual flair. Consider website performance and practicality in your design.
Content Hierarchy: Follow the suggested hierarchy based on provided copy, giving prominence to our key propositions while minimizing distractions.
Style: Maintain Lumora.io's colour scheme and font set, but we welcome fresh perspectives on how to apply them.
Copy: We will be providing new written copy to replace the current content on the website. The new design should complement and elevate the revised messaging.

Deliverables:
An initial homepage mock-up based on our brand guidelines.
Two rounds of feedback and revisions based on our input.
Final design files provided in Adobe XD (preferred) or Photoshop.

Brand Resources:
You will be given access to our Adobe Library, Brand Guidelines, and new website copy (and indicative wireframe), along with any necessary imagery from our stock library.
Note: please contact us if you would like access to our Adobe Library.

Number of Pages Required

1 page

Font styles to use
Sans Serif
Other font styles liked:
• Poppins Bold, Proxima Nova Light, Bold.

Colors

Designer to choose colors to be used in the design.

Requirements
Must have
• New website copy as supplied and ideally follow the wireframe provided. Aspirational visuals. Meets our brand guidelines
Should not have
• Stock standard imagery.

```html
<!DOCTYPE html>
<html lang="en">
<head>
<meta charset="utf-8">
<title>Lumora.io – Reach the Unreachable</title>
<link href="https://fonts.googleapis.com/css2?family=Montserrat:wght@400;500;600;700;800&family=Poppins:wght@600;700&display=swap" rel="stylesheet">
<style>
:root{
  --red:#e52a22;
  --red-dark:#c91f18;
  --ink:#1c1c1c;
  --text:#3a3a3a;
  --muted:#6b6b6b;
  --light:#f4f4f4;
  --line:#e6e6e6;
  --white:#ffffff;
  --navy:#141a2a;
}
*{margin:0;padding:0;box-sizing:border-box}
html,body{width:1200px;height:3850px;overflow:hidden;background:var(--white)}
body{font-family:"Montserrat",sans-serif;color:var(--ink);position:relative}
.abs{position:absolute}
.logo{font-family:"Poppins",sans-serif;font-weight:700;color:var(--red);letter-spacing:-1.5px}
.btn{display:inline-flex;align-items:center;justify-content:center;border-radius:30px;font-weight:700;font-size:11px;text-transform:uppercase;height:44px;padding:0 24px}
.btn-red{background:var(--red);color:var(--white)}
.btn-outline{border:2px solid var(--ink);color:var(--ink);background:var(--white)}
.btn-white{background:var(--white);color:var(--ink)}
.btn-ghost{border:2px solid var(--white);color:var(--white)}
.red{color:var(--red)}

/* top bar & nav */
.utility{left:622px;top:0;width:578px;height:42px;background:var(--red);border-bottom-left-radius:22px;color:var(--white);font-size:12px;font-weight:600;display:flex;align-items:center;gap:32px;padding-left:36px}
.utility .icons{margin-left:auto;margin-right:80px;display:flex;gap:18px}
.header-logo{left:88px;top:28px;font-size:56px}
.nav{left:545px;top:55px;display:flex;align-items:center;gap:26px;font-size:13px;font-weight:600}
.nav .demo{border:2px solid var(--ink);border-radius:24px;padding:12px 20px;font-size:11px;font-weight:700}

/* hero */
.hero{left:0;top:122px;width:1200px;height:582px;background:linear-gradient(110deg,#f6f6f6,#ececec);border-radius:0 60px 60px 60px}
.hero-photo{left:600px;top:100px;width:540px;height:615px;border-radius:260px 260px 0 0;background:linear-gradient(160deg,#f2c9c4 0%,#c9b3ad 45%,#8c8a93 100%)}
.hero-reach{left:84px;top:218px;font-family:"Poppins",sans-serif;font-weight:700;font-size:124px;line-height:1;color:var(--red)}
.hero-sub{left:88px;top:350px;font-size:50px;font-weight:600;color:var(--ink)}
.hero-lead{left:89px;top:418px;width:460px;font-size:22px;line-height:1.35;color:var(--text)}
.hero-solve{left:89px;top:488px;font-size:21px;font-weight:700;color:var(--red);border-bottom:2px solid var(--red);padding-bottom:2px}
.hero-note{left:89px;top:536px;width:480px;font-size:12.5px;line-height:1.5;color:var(--ink)}
.card{background:var(--white);border-radius:10px;box-shadow:0 10px 30px rgba(0,0,0,.1)}
.scroll-hint{left:590px;top:680px;width:20px;height:32px;border:2px solid var(--red);border-radius:12px}
.scroll-hint::after{content:"";position:absolute;left:7px;top:6px;width:2px;height:8px;background:var(--red)}

/* bridge */
.devices{left:150px;top:762px;width:404px;height:142px;border-radius:6px;background:linear-gradient(90deg,#2a2e3a,#4a5570 40%,#c8432f 75%,#20232b)}
.bridge-title{left:587px;top:788px;font-size:24px;font-weight:600;line-height:1.2;text-transform:uppercase}
.bridge-sub{left:587px;top:853px;font-size:11px;font-weight:500;text-transform:uppercase}
.bridge-links{left:587px;top:877px;font-size:10px;font-weight:700;display:flex;gap:20px;text-transform:uppercase}
.bridge-links span{border-bottom:1px solid currentColor}

/* emotive */
.emotive-title{left:87px;top:945px;font-size:36px;font-weight:600;text-transform:uppercase}
.arrow{width:40px;height:40px;border-radius:50%;display:flex;align-items:center;justify-content:center;color:var(--white);font-size:18px;font-weight:700}
.tabs{left:88px;top:1010px;display:flex;gap:12px}
.tab{height:58px;display:flex;align-items:center;justify-content:center;background:#e9e9e9;border-radius:6px;font-size:17px;font-weight:600;text-transform:uppercase;padding:0 34px;white-space:nowrap}
.tab.active{background:var(--red);color:var(--white)}
.emotive-bg{left:0;top:960px;width:1200px;height:586px;background:linear-gradient(180deg,#ffffff,#f6f6f6)}
.feature-photo{left:225px;top:1105px;width:345px;height:441px;border-radius:170px 170px 0 0;background:linear-gradient(170deg,#e7c49a 0%,#efd4c6 40%,#b9b2ad 100%)}
.halo{left:420px;top:1170px;width:160px;height:160px;border-radius:50%;border:26px solid #f0f0f0}
.badge{width:44px;height:44px;border-radius:50%;background:var(--white);box-shadow:0 4px 14px rgba(0,0,0,.12)}
.pr-card{left:88px;top:1263px;width:235px;height:204px;padding:18px}
.feature-h{left:677px;top:1236px;font-size:30px;font-weight:600;text-transform:uppercase}
.feature-p{left:677px;width:400px;font-size:15px;line-height:1.5;color:var(--text)}

/* red band */
.band{left:0;top:1546px;width:1200px;height:527px;background:linear-gradient(120deg,var(--red) 0%,#e0352b 60%,var(--red-dark) 100%);border-radius:26px 26px 26px 26px;color:var(--white)}
.band-head{left:0;top:1586px;width:1200px;text-align:center;font-size:22px;font-weight:700;line-height:1.35;text-transform:uppercase;color:var(--white)}
.band-rule{left:0;top:1673px;width:1200px;height:1px;background:rgba(255,255,255,.45)}
.band-title{left:176px;top:1738px;font-size:35px;font-weight:700;line-height:1.15;text-transform:uppercase;color:var(--white)}
.band-kicker{left:177px;top:1826px;font-size:19px;font-weight:700;color:var(--white)}
.band-copy{left:177px;top:1858px;width:400px;font-size:15px;line-height:1.45;color:var(--white)}
.band-photo{left:602px;top:1703px;width:560px;height:370px;border-radius:30px 30px 0 0;background:linear-gradient(140deg,#f4a7a0 0%,#e88a80 45%,#d96a5f 100%)}

/* platform */
.platform-title{left:0;top:2143px;width:1200px;text-align:center;font-size:35px;font-weight:700;line-height:1.17;text-transform:uppercase}
.tile{top:2254px;width:267px;height:271px;background:var(--white);border-radius:10px;box-shadow:0 8px 30px rgba(0,0,0,.08);text-align:center;padding:34px 26px 0}
.tile h3{font-size:13px;font-weight:700;text-transform:uppercase;line-height:1.35;margin-top:18px}
.tile p{font-size:13px;line-height:1.35;color:var(--text);margin-top:8px}
.dots{left:925px;top:2448px;width:110px;height:110px;background-image:radial-gradient(var(--red) 1.6px,transparent 1.8px);background-size:11px 11px;clip-path:polygon(85% 0,100% 0,100% 100%,0 100%,0 85%,85% 85%)}

/* complex */
.complex-title{left:0;top:2604px;width:1200px;text-align:center;font-size:22px;font-weight:600;line-height:1.35;text-transform:uppercase}
.orbit-logo{left:295px;top:2860px;font-size:56px}
.client{width:88px;height:88px;border-radius:50%}
.share-h{left:626px;top:2740px;font-size:36px;font-weight:700;line-height:1.18;text-transform:uppercase}
.share-k{left:627px;top:2838px;font-size:18px;font-weight:700;line-height:1.35;width:420px}
.share-p{left:627px;top:2895px;width:420px;font-size:15px;line-height:1.5;color:var(--text)}

/* cta */
.footer-bg{left:0;top:3280px;width:1200px;height:570px;background:var(--light)}
.cta{left:90px;top:3168px;width:1020px;height:200px;border-radius:22px;background:linear-gradient(120deg,var(--red),var(--red-dark));color:var(--white)}
.cta-title{left:139px;top:3204px;font-size:30px;font-weight:700;line-height:1.25;text-transform:uppercase;color:var(--white)}
.cta-sub{left:139px;top:3294px;font-size:17px;font-weight:700;color:var(--white)}

/* footer */
.col{top:3455px;font-size:12px;color:var(--text)}
.col h4{font-size:19px;font-weight:600;color:var(--ink);margin-bottom:18px}
.col li{list-style:none;margin-bottom:12.5px}
.social{width:34px;height:34px;border-radius:50%}
.copy{left:0;top:3792px;width:1200px;text-align:center;font-size:11px;color:var(--text)}
.chat{left:822px;top:3775px;width:288px;height:50px;border-radius:26px;background:#e5e5e5;display:flex;align-items:center;overflow:hidden;font-size:12px}
.chat span{flex:1;padding-left:22px;color:var(--muted)}
.chat b{background:var(--red);color:var(--white);height:100%;display:flex;align-items:center;padding:0 22px;font-size:12px;text-transform:uppercase}
.top-btn{left:1138px;top:3780px;width:40px;height:40px;border-radius:50%;background:var(--navy);color:var(--white);display:flex;align-items:center;justify-content:center;font-size:14px}
</style>
</head>
<body>

<!-- header -->
<div class="abs utility">
  <span>✉ Become a Partner</span><span>☎ Contact us</span>
  <span class="icons"><span>●</span><span>|</span><span>⌕</span></span>
</div>
<div class="abs logo header-logo">Lumora.io</div>
<nav class="abs nav">
  <span class="red">⌂</span><span>Platform ⌄</span><span>Solutions ⌄</span><span>Resources</span><span>About</span><span>Pricing</span><span class="demo">BOOK A DEMO</span>
</nav>

<!-- hero -->
<div class="abs hero"></div>
<div class="abs hero-photo" role="img" aria-label="Smiling businesswoman holding an open laptop"></div>
<div class="abs card" style="left:670px;top:228px;width:140px;height:128px;padding:14px 0 0;text-align:center">
  <svg width="80" height="80" viewBox="0 0 80 80"><circle cx="40" cy="40" r="32" fill="none" stroke="#eee" stroke-width="7"/><circle cx="40" cy="40" r="32" fill="none" stroke="var(--red)" stroke-width="7" stroke-dasharray="150 201" transform="rotate(-90 40 40)"/><text x="40" y="37" font-size="7" font-weight="700" text-anchor="middle" font-family="Montserrat">SEE</text><text x="40" y="45" font-size="7" font-weight="700" text-anchor="middle" font-family="Montserrat">WHAT'S</text><text x="40" y="53" font-size="7" font-weight="700" text-anchor="middle" font-family="Montserrat">TRENDING</text></svg>
  <div style="font-size:8px;margin-top:4px">1546 Views <span class="red">•</span> 746 Clicks</div>
</div>
<div class="abs card" style="left:950px;top:476px;width:195px;height:68px;padding:10px 12px">
  <div style="font-size:10px;font-weight:600">Status</div>
  <svg width="170" height="36" viewBox="0 0 170 36"><path d="M2 26 Q12 10 22 24 T42 22 T62 20 T82 26 T102 16 T122 24 T142 14 T168 8" fill="none" stroke="var(--red)" stroke-width="2"/></svg>
</div>
<div class="abs card" style="left:572px;top:505px;width:228px;height:130px"></div>
<div class="abs hero-reach">Reach</div>
<div class="abs hero-sub">The Unreachable.</div>
<p class="abs hero-lead">You know you have a problem. We know why you have a problem.</p>
<div class="abs hero-solve">Let's solve it together.</div>
<p class="abs hero-note">You're not here by accident. You're also not alone. Many large, complex businesses are facing the same communication challenges... <span class="red" style="font-weight:600">&lt;more&gt;</span></p>
<div class="abs scroll-hint"></div>

<!-- bridge -->
<div class="abs devices" role="img" aria-label="Screens, laptop and phone showing workplace content"></div>
<h2 class="abs bridge-title">Lumora enables you to<br>bridge <span class="red">the communication</span> gap</h2>
<div class="abs bridge-sub">and develop a more informed, aligned and inspired workplace.</div>
<div class="abs bridge-links"><span class="red">Book a demo</span><span>Watch video (4:40)</span></div>

<!-- emotive -->
<div class="abs emotive-bg"></div>
<h2 class="abs emotive-title">Emotive Feature</h2>
<div class="abs arrow" style="left:1026px;top:943px;background:var(--navy)">‹</div>
<div class="abs arrow" style="left:1072px;top:943px;background:var(--red)">›</div>
<div class="abs tabs">
  <div class="tab" style="width:280px">Manage the Culture</div>
  <div class="tab" style="width:225px">Calm the Noise</div>
  <div class="tab" style="width:262px">Change Behaviour</div>
  <div class="tab active" style="width:240px">Inspire &amp; Excite</div>
  <div class="tab" style="width:120px;justify-content:flex-start;padding-left:36px">In</div>
</div>
<div class="abs halo"></div>
<div class="abs feature-photo" role="img" aria-label="Young woman in a sun hat smiling at her phone"></div>
<div class="abs badge" style="left:480px;top:1188px"></div>
<div class="abs badge" style="left:566px;top:1212px"></div>
<div class="abs badge" style="left:585px;top:1292px"></div>
<div class="abs badge" style="left:517px;top:1348px"></div>
<div class="abs card pr-card">
  <div style="font-size:14px;font-weight:700">PR Views</div>
  <svg width="200" height="150" viewBox="0 0 200 150" style="margin-top:6px" font-family="Montserrat" font-size="7">
    <text x="0" y="29">10K</text><text x="0" y="59">05K</text><text x="0" y="90">2.5K</text><text x="0" y="119">01K</text>
    <g fill="#dfe3ec">
      <rect x="30" y="70" width="11" height="48"/><rect x="49" y="58" width="11" height="60"/><rect x="68" y="64" width="11" height="54"/><rect x="87" y="74" width="11" height="44"/><rect x="106" y="90" width="11" height="28"/><rect x="125" y="40" width="11" height="78"/><rect x="163" y="60" width="11" height="58"/>
    </g>
    <rect x="144" y="46" width="11" height="72" fill="var(--red)"/>
    <rect x="133" y="22" width="34" height="14" rx="2" fill="#fff" stroke="var(--red)"/><text x="150" y="32" text-anchor="middle" fill="var(--red)" font-size="8">5,200</text>
    <g text-anchor="middle"><text x="35" y="136">10</text><text x="54" y="136">11</text><text x="73" y="136">12</text><text x="92" y="136">13</text><text x="111" y="136">14</text><text x="130" y="136">15</text><text x="149" y="136">16</text><text x="168" y="136">17</text><text x="187" y="136">18</text></g>
  </svg>
</div>
<h2 class="abs feature-h">Inspire &amp; Excite</h2>
<p class="abs feature-p" style="top:1282px">Ever felt uplifted by an email blast? Or inspired by a text message?</p>
<p class="abs feature-p" style="top:1337px">Using vibrant visuals to deliver timely and engaging screen content, you can generate excitement and motivate your workforce.</p>
<div class="abs btn btn-red" style="left:678px;top:1424px">Book a demo</div>

<!-- red band -->
<div class="abs band"></div>
<h2 class="abs band-head">Lumora is the one workplace comms platform that<br>reaches &amp; engages everyone,everywhere.</h2>
<div class="abs band-rule"></div>
<h2 class="abs band-title">Transform<br>how you connect</h2>
<div class="abs band-kicker">with hard-to-reach workers.</div>
<p class="abs band-copy">Lumora brings together digital workplace screens, desktops and mobiles to reach all your people – whether they're at home at their desks, on the road or the factory floor.</p>
<div class="abs btn btn-white" style="left:179px;top:1960px">Book a demo</div>
<div class="abs band-photo" role="img" aria-label="Excited young woman with phone beside app screens and a file upload menu"></div>

<!-- platform -->
<h2 class="abs platform-title">A <span class="red">single platform</span> for all<br>your key teams.</h2>
<div class="abs dots"></div>
<div class="abs tile" style="left:182px">
  <svg width="80" height="80" viewBox="0 0 80 80" fill="none" stroke="var(--ink)" stroke-width="2.5"><circle cx="40" cy="12" r="6"/><circle cx="16" cy="50" r="6"/><circle cx="64" cy="50" r="6"/><path d="M6 72c0-8 5-12 10-12s10 4 10 12M54 72c0-8 5-12 10-12s10 4 10 12"/><rect x="26" y="28" width="28" height="18" rx="5" stroke="var(--red)"/><path d="M33 37h14" stroke="var(--red)"/></svg>
  <h3>Lumora works for internal comms teams</h3>
  <p>Always pushed for time, often stretched for resources and people – Lumora takes a huge load off.</p>
</div>
<div class="abs tile" style="left:466px">
  <svg width="80" height="80" viewBox="0 0 80 80" fill="none" stroke="var(--red)" stroke-width="2.5"><rect x="10" y="18" width="60" height="40" rx="3"/><path d="M32 70h16M40 58v12"/><path d="M28 44l12-18 12 18z" stroke="var(--ink)"/><circle cx="40" cy="10" r="4" stroke="var(--ink)"/></svg>
  <h3>No need to play graphic designer</h3>
  <p>Lumora gives you access to an extensive library of templates, for effortless creation of stunning content.</p>
</div>
<div class="abs tile" style="left:749px">
  <svg width="80" height="80" viewBox="0 0 80 80" fill="none" stroke="var(--ink)" stroke-width="2.5"><path d="M8 30h28v40H8zM44 30h28v40H44z"/><path d="M14 40h16M14 50h16M50 40h16M50 50h16"/><circle cx="40" cy="16" r="9"/><path d="M37 25v5h6v-5"/></svg>
  <h3>Bite-sized content for snackable learning</h3>
  <p>Lumora's snackable learning framework delivers messages that are optimally sized and sequenced for uptake.</p>
</div>

<!-- complex businesses -->
<h2 class="abs complex-title">Lumora works for large, <span class="red">complex businesses</span><br>and it will work for you, too.</h2>
<svg class="abs" style="left:190px;top:2700px" width="380" height="380" viewBox="0 0 380 380" fill="none" stroke="var(--ink)" stroke-width="2">
  <path d="M70 80 A170 170 0 0 0 40 280"/><path d="M90 120 A130 130 0 0 0 60 220"/><path d="M300 70 A170 170 0 0 1 350 200"/><path d="M320 260 A170 170 0 0 1 200 340"/><path d="M140 345 A170 170 0 0 0 250 330"/>
  <circle cx="70" cy="80" r="3" fill="var(--ink)"/><circle cx="350" cy="200" r="3" fill="var(--ink)"/>
</svg>
<div class="abs logo orbit-logo">Lumora.io</div>
<div class="abs client" style="left:325px;top:2685px;background:#1f6b3a"></div>
<div class="abs client" style="left:497px;top:2795px;width:66px;height:66px;background:#f6cd16"></div>
<div class="abs client" style="left:170px;top:2848px;width:84px;height:84px;background:#e9442f"></div>
<div class="abs client" style="left:242px;top:2986px;width:100px;height:100px;background:#1d64b8"></div>
<div class="abs client" style="left:430px;top:2996px;width:72px;height:72px;background:#f1f1f1"></div>
<h2 class="abs share-h">We can easily<br>share information</h2>
<div class="abs share-k">to staff across New Zealand that isn't always available to them.</div>
<p class="abs share-p">The different templates are a bonus - there's always a layout that works with what you want to share.</p>
<div class="abs btn btn-red" style="left:627px;top:2948px">Book a demo</div>
<div class="abs btn btn-outline" style="left:767px;top:2948px">Free trial</div>

<!-- cta -->
<div class="abs footer-bg"></div>
<div class="abs cta"></div>
<h2 class="abs cta-title">Transform the way<br>you talk to your workforce.</h2>
<div class="abs cta-sub">Lumora will enable you to reach &amp; engage everyone, everywhere.</div>
<div class="abs btn btn-white" style="left:748px;top:3248px;width:155px">Book a demo</div>
<div class="abs btn btn-ghost" style="left:913px;top:3248px;width:155px">Find out more</div>

<!-- footer -->
<div class="abs logo" style="left:88px;top:3550px;font-size:44px">Lumora.io</div>
<div class="abs social" style="left:107px;top:3617px;background:var(--navy)"></div>
<div class="abs social" style="left:150px;top:3617px;background:var(--red)"></div>
<div class="abs social" style="left:192px;top:3617px;background:var(--navy)"></div>
<ul class="abs col" style="left:321px"><h4>Lumora.io</h4><li>Platform Overview</li><li>Features</li><li>Security</li><li>Workplace Digital Signage Screens</li><li>Corporate Screensavers</li><li>Template Library</li><li>Integrations</li><li>Infotainment Streams</li><li>Premium Programs</li></ul>
<ul class="abs col" style="left:567px"><h4>Who we're for</h4><li>Industrial &amp; Manufacturing</li><li>Mining &amp; Construction</li><li>Government &amp; Public Sector</li><li>Aged Care</li><li>Logistics</li><li>Retail</li></ul>
<ul class="abs col" style="left:783px"><h4>Resources</h4><li>Latest Insights</li><li>Snackable Learning Framework</li><li>Help Centre</li><li>Server Status</li><li>Privacy Policy</li><li>Terms &amp; Service</li></ul>
<ul class="abs col" style="left:998px"><h4>Get Started</h4><li>Book a Demo</li><li>Free Trial</li><li>Pricing</li><li>Become a Partner</li><li>Contact Us</li></ul>
<div class="abs copy">© 2024 Lumora.io Limited All rights reserved</div>
<div class="abs chat"><span>Need help?</span><b>Chat now</b></div>
<div class="abs top-btn">⌃</div>

</body>
</html>
```